Packaging Box for LED Lighted Terrarium Kit

Need to design a packaging box

Target Market(s)

children

Requirements
Must have
• see instruction sheet
Nice to have
• colorful

```html
<!DOCTYPE html>
<html lang="en">
<head>
<meta charset="utf-8">
<title>LED Lighted Terrarium Kit – Box Dieline</title>
<link href="https://fonts.googleapis.com/css2?family=Roboto+Slab:wght@800&family=Roboto+Condensed:wght@400;700&family=Tinos&display=swap" rel="stylesheet">
<style>
:root{
  --paper:#ffffff;
  --cut:#4a4a4a;
  --slab-grey:#3a3a3a;
  --age-grey:#8a8a8a;
  --night-top:#2a2664;
  --night-mid:#4a3f93;
  --night-low:#1c1b4a;
  --meadow-light:#e6e77a;
  --meadow-top:#c7c73a;
  --meadow-mid:#9ebf2e;
  --grass:#5aad30;
  --grass-dark:#3a8a22;
  --jar-blue:#5fa6e6;
  --jar-glass:#e3e8ef;
  --jar-warm:#c79a6e;
  --brand-red:#e02020;
  --accent-red:#e8221b;
  --badge:#f3a21c;
}
*{box-sizing:border-box;margin:0;padding:0}
html,body{width:1200px;height:650px;overflow:hidden;background:var(--paper)}
.canvas{position:relative;width:1200px;height:650px;background:var(--paper)}
.size-label{position:absolute;left:38px;top:82px;font-family:"Tinos",serif;font-size:33px;color:#111;letter-spacing:.5px}
.panel{position:absolute;top:259px;height:181px;overflow:hidden}
.art{position:absolute}
.jar{position:absolute;border-radius:12px;
  background:linear-gradient(180deg,var(--jar-blue),var(--jar-glass) 30%,var(--jar-glass) 55%,var(--jar-warm))}
.title{position:absolute;font-family:"Roboto Slab",serif;font-weight:800;font-size:12px;line-height:13.5px;text-align:right;white-space:nowrap}
.brand{position:absolute;background:#fff;font-family:"Roboto Slab",serif;font-weight:800;font-size:8.5px;color:var(--brand-red);padding:2px 4px;display:flex;align-items:center;gap:3px;white-space:nowrap}
.brand i{display:block;width:6px;height:6px;border-radius:50%;background:var(--brand-red)}
.age{position:absolute;font-family:"Roboto Slab",serif;font-weight:800;font-size:10px;color:var(--age-grey)}
.badge{position:absolute;width:48px;height:28px;border-radius:4px;background:var(--badge)}

.panel-night{left:26px;width:276px;background:linear-gradient(180deg,var(--night-top),var(--night-mid) 55%,var(--night-low))}
.panel-night .title{color:#fff}
.panel-front{left:302px;width:282px;background:var(--paper)}
.panel-front .title{color:var(--slab-grey)}
.panel-meadow{left:584px;width:277px;background:linear-gradient(180deg,var(--meadow-light),var(--meadow-top) 50%,var(--meadow-mid) 78%,var(--grass-dark))}
.panel-meadow .title{color:#fff}
.panel-info{left:861px;width:280px;background:var(--paper);font-family:"Roboto Condensed",sans-serif;color:#333}
.info-col{position:absolute;top:9px;font-size:3.6px;line-height:4.6px}
.info-col h3{font-size:4.6px;font-weight:400;color:var(--accent-red);margin:3px 0 1px}
.info-col p{margin-bottom:2px}
.items{position:absolute;left:187px;top:11px;width:90px;display:grid;grid-template-columns:1fr 1fr;row-gap:3px;column-gap:3px}
.item{display:flex;align-items:center;gap:3px;height:15px;border-bottom:.5px dashed #999;font-size:3.2px;line-height:3.6px;text-transform:uppercase}
.item b{flex:0 0 11px;height:11px;border-radius:50%;font-weight:400}

.lid{position:absolute;left:305px;top:75px;width:279px;height:184px;overflow:hidden;transform:rotate(180deg);background:var(--paper)}
.lid .title{color:var(--slab-grey)}

.dieline{position:absolute;left:0;top:0;pointer-events:none}
.dieline path{fill:none;stroke:var(--cut);stroke-width:.8}
</style>
</head>
<body>
<div class="canvas">
  <div class="size-label">16.8*11*17</div>

  <!-- lid (printed upside down on the net) -->
  <div class="lid">
    <div class="art" role="img" aria-label="Grass and hanging plants photo" style="left:0;top:120px;width:279px;height:64px;background:linear-gradient(180deg,rgba(90,173,48,0),var(--grass) 70%)"></div>
    <div class="jar" role="img" aria-label="Product photo of the filled terrarium jar" style="left:102px;top:18px;width:96px;height:160px"></div>
    <div class="badge" style="left:24px;top:34px"></div>
    <div class="age" style="left:230px;top:42px">Age6+</div>
    <div class="title" style="right:188px;top:100px">LED<br>Lighted<br>Terrarium Kit</div>
    <div class="brand" style="left:8px;top:160px"><i></i>Bright Sprout Kits</div>
  </div>

  <!-- side panel: night -->
  <section class="panel panel-night">
    <div class="art" role="img" aria-label="Night landscape photo behind the jar" style="inset:0"></div>
    <div class="jar" role="img" aria-label="Glowing terrarium jar photo" style="left:143px;top:20px;width:84px;height:146px;background:linear-gradient(180deg,#8fb8ee,#d9d2f2 45%,#b99274)"></div>
    <div class="title" style="right:142px;top:116px">LED<br>Lighted<br>Terrarium Kit</div>
  </section>

  <!-- front panel -->
  <section class="panel panel-front">
    <div class="art" role="img" aria-label="Grass and leafy plants photo" style="left:0;top:110px;width:282px;height:71px;background:linear-gradient(180deg,rgba(90,173,48,0),var(--grass) 75%)"></div>
    <div class="jar" role="img" aria-label="Product photo of the filled terrarium jar" style="left:101px;top:12px;width:96px;height:160px"></div>
    <div class="badge" style="left:26px;top:16px"></div>
    <div class="age" style="left:234px;top:29px">Age6+</div>
    <div class="title" style="right:190px;top:102px">LED<br>Lighted<br>Terrarium Kit</div>
    <div class="brand" style="left:9px;top:162px"><i></i>Bright Sprout Kits</div>
  </section>

  <!-- side panel: meadow -->
  <section class="panel panel-meadow">
    <div class="art" role="img" aria-label="Sunny meadow photo behind the jar" style="inset:0"></div>
    <div class="jar" role="img" aria-label="Product photo of the filled terrarium jar" style="left:145px;top:8px;width:96px;height:164px"></div>
    <div class="title" style="right:139px;top:24px">LED<br>Lighted<br>Terrarium Kit</div>
  </section>

  <!-- back panel: instructions -->
  <section class="panel panel-info">
    <div class="info-col" style="left:11px;width:92px">
      <h3 style="margin-top:0">What is a terrarium?</h3>
      <p>A terrarium is a small tabletop garden in a container that copies the natural world outside. It is a slice of nature small enough to hold in your hands.</p>
      <p>Terrariums can live in any glass container. This light-up kit is the perfect size to watch a tiny ecosystem grow right on your desk.</p>
      <p>Once planted, you will see how plants grow and how fun gardening can be. Build it today and enjoy weeks of science fun!</p>
      <h3>Your terrarium is all done!</h3>
      <p>Place it in a sunny spot and spray a little water every day. Charge the lid before night. Seeds take about 3-4 days to sprout.</p>
      <h3>HELPFUL HINTS</h3>
      <p>• Keep the terrarium in a warm, sunny place.</p>
      <p>• No sprouts? Check the soil and spray more water.</p>
      <p>• Too wet? Lift the lid and let the soil dry a bit.</p>
    </div>
    <div class="info-col" style="left:108px;width:70px">
      <h3 style="margin-top:0">How to make your terrarium glow!</h3>
      <p>The lid has star cutouts for air and a small light inside. Charge it with the USB cable; a full charge takes 2-3 hours.</p>
      <p>Flip the switch next to the port and the light shines for about 4 hours. Enjoy your glowing mini garden!</p>
      <h3>Tip: <span style="color:#333">Do not overcharge the battery.</span></h3>
      <h3>Warning: <span style="color:#333">Do not open the battery casing.</span></h3>
    </div>
    <div class="jar" role="img" aria-label="Small photo of the finished terrarium" style="left:124px;top:123px;width:35px;height:55px;border-radius:6px"></div>
    <div class="items">
      <div class="item"><b style="background:#eee;border:.5px solid #ccc"></b>Jar</div>
      <div class="item"><b style="background:#3a8fe0"></b>Light-up jar lid</div>
      <div class="item"><b style="background:#ddd"></b>Micro-USB charging cable</div>
      <div class="item"><b style="background:#7a4a2a"></b>Soil</div>
      <div class="item"><b style="background:#f07a18"></b>Orange sand</div>
      <div class="item"><b style="background:#e5e0d8"></b>White river rocks</div>
      <div class="item"><b style="background:#555"></b>Chia seeds</div>
      <div class="item"><b style="background:#7b5a38"></b>Wheatgrass seeds</div>
      <div class="item"><b style="background:#e8e8e8"></b>Spray bottle</div>
      <div class="item"><b style="background:#3a8fe0"></b>Small stick</div>
      <div class="item"><b style="background:#eee"></b>Miniature bunny</div>
      <div class="item"><b style="background:#a5592a"></b>Miniature deer</div>
      <div class="item"><b style="background:#9bc95a"></b>Decorative stickers</div>
      <div class="item"><b style="background:#d42a2a"></b>Miniature mushroom house</div>
    </div>
  </section>

  <!-- cut lines -->
  <svg class="dieline" width="1200" height="650" viewBox="0 0 1200 650">
    <path d="M305 75 L307 60 Q309 38 330 38 L560 38 Q581 38 582 60 L584 75"/>
    <path d="M305 75 L321 75 L321 73 M415 75 L415 72 L470 72 L470 75 M568 73 L568 75 L584 75"/>
    <path d="M305 75 L305 259 M584 75 L584 259"/>
    <path d="M26 259 L47 169 L302 169 L302 259"/>
    <path d="M588 259 L588 169 L837 169 L861 259"/>
    <path d="M977 259 L977 244 Q977 234 987 234 L1022 234 Q1031 234 1031 244 L1031 259"/>
    <path d="M26 259 L1141 259 M26 440 L1141 440 M26 259 L26 440 M1141 259 L1141 440"/>
    <path d="M1141 259 L1182 270 L1182 432 L1141 440"/>
    <path d="M26 440 L26 564 L150 564 Q159 564 159 555 L159 516 L294 440"/>
    <path d="M301 440 L301 612 L366 612 Q378 612 378 600 L378 576 L504 576 L504 600 Q504 612 516 612 L580 612 L580 440"/>
    <path d="M589 440 L722 516 L722 555 Q722 563 731 563 L857 563 L857 440"/>
    <path d="M863 440 L938 575 L938 600 Q938 612 950 612 L1050 612 Q1062 612 1062 600 L1062 575 L1141 440"/>
  </svg>
</div>
</body>
</html>
```